Plox, an electronic music website !

Hi there,
We are an events agenda (festivals & parties...) specialized in all kinds of electronic music.
It's a big database where peoples come to search there next party and post comments, photos and carpoolings.
Users are between 16 and 45 years old for most of them but the majority is between 18 and 35.
They all love techno music and partying,
We are looking for a design for 2 similar pages.
PSD Uncoded design only for "homepage" and "event page".
Something cool & young but serious and clear.
Thanks

Industry/Entity Type

Events

Number of Pages Required

2 page

Font styles to use
Sans Serif

Requirements
Must have
• Homepage
• - Logo + Name (Black and White logo)
• - Banner (1428x528px in 96ppp or proportional smaller dimension)
• - Slogan "electronic events database" (find police)
• - Principal menu with : « Events », « Map », « Carpooling », « Photos » and « Infos/Contact »
• and
• - Research table (most important) with :
• « Event name », « Kind of music », « Number of people », « Date », « Continent », « Country » and an « advanced search » link.
• - A connexion zone for accounts (Sign In) and a « create account » link.
• - Some social media direct links (Lindrav, Vimzo+ and Quenlo)
• - A "focus" zone to present a special event once a month with :
• « Name », « picture (flyer) », « location », « country », « date », « kind of music », the Movara video, and a "more infos" link.
• - An "incoming" zone, with an events list (next ones, 6 or 8) :
• one line per event and, on each line :
• « Name », « picture (flyer) », « location », « country (flag) », « date » and a "more infos" link.
• - A "carpooling" zone, with the list of next carpooling (3 or 4) with on each line :
• « Event name », « picture (flyer) », « country », « date », « seats » and a « more info » link.
• - A map link picture.
• - A calendar (small and easy to understand)
• - A link to photos (only the lasts albums).
• We need a new design for this page, I put a picture of an old design I did by myself (with Paint) just to have an idea. We just want exactly the same things there is on the picture but you can move and change all elements and colors.
• This page is too long for me.
• Page 2 (Event page) : with the document « New » and « Old event page »
• Second most important page
• A lot of things on this page :
• and
• - Event name
• - Flyer (960x960px in 96ppp or proportional dimension)
• - Links to « official website », « tickets » and « add a carpooling »
• - Event informations :
• Location (Continent, Country, Adress)
• Date (from… to…)
• Kind of music
• Number of people
• Price (regular)
• Camping (yes or no)
• - Video Movara
• - Description (long text with lineup and others informations)
• - Carpoolings availables (+ an other link to add a new one)
• - Photos (+ a link to add some)
• - Others similar events (few names)
• - A « Comments » zone where users can whrite what they think about the event.
• Same thing, I made an exemple for this page, please make a new design.
• (Sorry, the website on the document is in French)
• Thanks ;)

```html
<!DOCTYPE html>
<html lang="en">
<head>
<meta charset="utf-8">
<title>Plox – Electronic Events Database</title>
<link href="https://fonts.googleapis.com/css2?family=Cinzel:wght@400;700&family=Lato:wght@400;700&family=Merriweather:wght@900&family=Kaushan+Script&family=Crimson+Text:wght@400;600&display=swap" rel="stylesheet">
<style>
:root{
  --white:#ffffff;
  --ink:#222222;
  --muted:#8a8a8a;
  --blue:#2c86c0;
  --blue-dark:#1f6fa3;
  --cyan:#4fb8e8;
  --night:#121314;
  --night-2:#262829;
  --navy:#0f2f45;
  --navy-2:#133a54;
  --footer:#1c1d1e;
  --line:#d7d7d7;
}
*{margin:0;padding:0;box-sizing:border-box}
html,body{width:1200px;height:2719px;overflow:hidden;background:var(--night)}
body{position:relative;font-family:'Lato',sans-serif;color:var(--ink)}
.abs{position:absolute}

/* top bar */
.topbar{left:0;top:0;width:1200px;height:36px;background:var(--white);border-bottom:1px solid #e5e5e5}
.social{left:108px;top:9px;display:flex;gap:8px;font-size:11px;color:var(--blue-dark)}
.social span{display:flex;align-items:center;gap:4px}
.social span::before{content:"";width:8px;height:8px;border-radius:50%;background:var(--blue-dark)}
.account{right:108px;top:0;height:36px;display:flex;align-items:center;gap:22px;font-size:11px;color:#555}
.account .lang{width:22px;height:14px;background:#3b4e8a}

/* hero */
.hero{left:0;top:36px;width:1200px;height:444px;background:radial-gradient(ellipse at 55% 25%,#d9c4a3 0%,#8a7158 30%,#3a2d24 62%,#140f0c 100%)}
.brand{left:300px;top:60px;display:flex;align-items:center;gap:22px}
.brand .name{font-family:'Lato',sans-serif;font-weight:700;font-size:56px;color:#111;width:130px;text-align:center}
.tagline{display:flex;flex-direction:column;align-items:center}
.tagline h1{font-family:'Merriweather',serif;font-weight:900;font-size:38px;color:#111;letter-spacing:.5px}
.tagline p{font-family:'Kaushan Script',cursive;font-size:26px;color:#111;margin-top:2px;margin-left:140px}

/* nav */
.nav{left:0;top:480px;width:1200px;height:58px;background:var(--white)}
.nav ul{list-style:none;position:absolute;left:108px;top:12px;display:flex;height:34px;border-left:1px solid var(--line)}
.nav li{font-family:'Cinzel',serif;font-size:13px;letter-spacing:1px;color:#555;display:flex;align-items:center;justify-content:center;border-right:1px solid var(--line);height:34px}
.nav li.active span{background:var(--blue);color:var(--white);padding:8px 24px;font-weight:700}

/* dark band */
.dark{left:0;top:538px;width:1200px;height:894px;background:linear-gradient(90deg,#0d0e0f,#2a2c2d 30%,#161718 55%,#2c2e2f 80%,#0e0f10)}

/* search */
.search{left:110px;top:582px;width:980px;height:254px;background:var(--white);border-radius:4px}
.search-box{left:12px;top:10px;width:734px;height:234px;border:1px solid #dcdcdc}
.search-box h2{position:absolute;left:14px;top:12px;font-family:'Cinzel',serif;font-size:25px;color:var(--blue);font-weight:400}
.search-box h2 small{font-family:'Lato',sans-serif;font-size:11px;color:#333;margin-left:10px;vertical-align:middle}
.field{position:absolute;width:336px;height:26px;border:1px solid #999;font-size:10px;color:#666;padding:6px 18px}
.field.select::after{content:"";position:absolute;right:0;top:0;width:24px;height:24px;background:#888}
.field.select::before{content:"";position:absolute;right:7px;top:9px;border:5px solid transparent;border-top-color:#fff;z-index:1}
.check{position:absolute;left:26px;top:170px;font-size:10px;color:#444;display:flex;align-items:center;gap:8px}
.check i{width:9px;height:9px;border:1px solid #777}
.btn-blue{position:absolute;background:var(--blue);color:var(--white);font-size:12px;display:flex;align-items:center;justify-content:center;border-radius:2px}
.add-event{left:778px;top:22px;width:169px;height:30px;font-family:'Cinzel',serif;font-size:15px;letter-spacing:1px}
.calendar{left:767px;top:67px;width:193px;border:1px solid #cfcfcf;font-size:9px}
.calendar .head{background:var(--blue);color:var(--white);text-align:center;height:22px;line-height:22px;font-weight:700;font-size:10px}
.calendar table{width:100%;border-collapse:collapse;text-align:center}
.calendar th{font-weight:400;height:18px;color:#333}
.calendar td{height:19px;color:#222;border-top:1px solid #eee}
.calendar td.off{color:#aaa}
.calendar td.today{color:var(--blue);font-weight:700}

/* section titles */
.section-title{width:1200px;left:0;text-align:center;font-family:'Cinzel',serif;font-size:27px;color:var(--white);letter-spacing:1px}
.section-title::after{content:"";display:block;width:290px;height:1px;background:rgba(255,255,255,.6);margin:8px auto 0}

/* special events */
.arrow{top:1130px}
.card{top:937px;width:312px;height:463px;border:1px solid #777;padding:8px}
.card .inner{width:100%;height:100%;border:1px solid #666;background:#0c0c0d}
.card .photo{height:308px}
.card h3{font-family:'Crimson Text',serif;font-weight:400;font-size:21px;color:var(--cyan);margin:14px 0 8px 18px}
.meta{display:flex;align-items:center;gap:8px;font-size:10px;color:#ddd;margin:0 0 10px 22px}
.meta svg{flex:none}
.meta .gap{margin-left:32px}

/* videos */
.videos{left:0;top:1432px;width:1200px;height:490px;background:linear-gradient(180deg,#0b1a2a,#1c3550 45%,#0d1520)}
.video{width:312px;height:145px;border:1px solid #556}
.video .date{position:absolute;left:12px;bottom:10px;color:var(--white);font-weight:700;font-size:12px}
.play{position:absolute;left:50%;top:50%;width:36px;height:26px;margin:-13px 0 0 -18px;background:#d3202a;border-radius:6px}
.play::after{content:"";position:absolute;left:14px;top:7px;border:6px solid transparent;border-left:10px solid #fff;border-right:0}
.featured .label{position:absolute;left:16px;top:108px;color:#fff;font-size:12px}
.featured .label small{display:block;font-size:9px;color:#ccc;margin-top:4px}
.featured .bar{position:absolute;left:0;bottom:0;width:100%;height:36px;background:rgba(0,0,0,.55);display:flex;gap:12px;padding:8px 14px}
.featured .bar span{border:1px solid #aaa;color:#eee;font-size:9px;padding:4px 14px}
.btn-outline-blue{border:1px solid #9cd2f0}

/* upcoming */
.upcoming{left:0;top:1922px;width:1200px;height:538px;background:linear-gradient(180deg,var(--navy-2),var(--navy))}
.event-img{width:225px;height:138px;border:1px solid #4b6a80}
.event-info{width:235px}
.event-info h3{font-family:'Crimson Text',serif;font-weight:600;font-size:24px;color:var(--white);margin-bottom:12px}
.event-info .meta{margin-left:0;color:#e5e5e5}
.ev-btns{display:flex;gap:14px;margin-top:14px}
.ev-btns span{border:1px solid #ddd;color:#fff;font-size:14px;width:100px;height:34px;display:flex;align-items:center;justify-content:center;border-radius:2px}
.ev-btns span+span{width:102px}
.divider{left:109px;top:2203px;width:982px;height:1px;background:#2f5572}

/* footer */
.footer{left:0;top:2460px;width:1200px;height:223px;background:linear-gradient(90deg,#151617,#2a2b2c 40%,#1a1b1c)}
.fcol h4{font-size:13px;font-weight:700;color:var(--white);margin-bottom:12px}
.fcol h4::after{content:"";display:block;width:100px;height:1px;background:#555;margin-top:8px}
.links li{list-style:none;font-size:11px;color:#ddd;line-height:24px}
.links li::before{content:"›";margin-right:8px;color:#aaa}
.fcol p{font-size:11px;color:#ddd;line-height:16px}
.email{margin-top:14px;width:190px;height:27px;background:#fff;font-size:10px;color:#555;padding:7px 8px;font-style:italic}
.subscribe{margin-top:12px;width:84px;height:22px;font-size:10px;font-weight:700;position:static}
.contact-row{display:flex;gap:14px;align-items:flex-start;font-size:11px;color:#ddd;margin-bottom:12px}
.bottom{left:0;top:2683px;width:1200px;height:36px;background:var(--blue-dark);color:#fff;font-size:11px}
</style>
</head>
<body>

<div class="abs topbar">
  <div class="abs social"><span>Lindrav</span><span>Quenlo</span><span>Vimzo+</span></div>
  <div class="abs account"><span>Sign In</span><span>Create Account</span><span class="lang"></span></div>
</div>

<div class="abs hero" role="img" aria-label="Crowd with raised hands at a concert under warm stage lights">
  <div class="abs brand">
    <div class="name">Plox</div>
    <div class="tagline">
      <h1>Electronic Events Database</h1>
      <p>Festivals &amp; Parties Agenda</p>
    </div>
  </div>
</div>

<nav class="abs nav">
  <ul>
    <li class="active" style="width:130px"><span>Home</span></li>
    <li style="width:130px">Events</li>
    <li style="width:110px">Map</li>
    <li style="width:160px">Carpooling</li>
    <li style="width:130px">Photos</li>
    <li style="width:110px">Infos</li>
    <li style="width:150px">Contact</li>
  </ul>
</nav>

<div class="abs dark"></div>

<section class="abs search">
  <div class="abs search-box">
    <h2>Search Table <small>(au moins un des champs ci-dessous)</small></h2>
    <div class="field" style="left:26px;top:64px">Nom Du Festival</div>
    <div class="field select" style="left:392px;top:64px">Nombre De Personne</div>
    <div class="field select" style="left:26px;top:101px">Type De Musique</div>
    <div class="field select" style="left:392px;top:101px">Continent</div>
    <div class="field select" style="left:26px;top:138px">Date</div>
    <div class="field select" style="left:392px;top:138px">Pays</div>
    <div class="check"><i></i>sur plusieurs jours</div>
    <div class="btn-blue" style="left:26px;top:195px;width:84px;height:28px">Search</div>
  </div>
  <div class="btn-blue add-event">Add Event</div>
  <div class="abs calendar">
    <div class="head">June 2011</div>
    <table>
      <tr><th>Mon</th><th>Tue</th><th>Wed</th><th>Thu</th><th>Fri</th><th>Sat</th><th>Sun</th></tr>
      <tr><td class="off">30</td><td class="off">31</td><td>1</td><td>2</td><td>3</td><td>4</td><td>5</td></tr>
      <tr><td>6</td><td>7</td><td class="today">8</td><td>9</td><td>10</td><td>11</td><td>12</td></tr>
      <tr><td>13</td><td>14</td><td>15</td><td>16</td><td>17</td><td>18</td><td>19</td></tr>
      <tr><td>20</td><td>21</td><td>22</td><td>23</td><td>24</td><td>25</td><td>26</td></tr>
      <tr><td>27</td><td>28</td><td>29</td><td>30</td><td class="off">1</td><td class="off">2</td><td class="off">3</td></tr>
    </table>
  </div>
</section>

<h2 class="abs section-title" style="top:868px">Present Special Event</h2>

<svg class="abs arrow" style="left:50px" width="22" height="40" viewBox="0 0 22 40"><path d="M18 2 4 20l14 18" fill="none" stroke="#bbb" stroke-width="2"/></svg>
<svg class="abs arrow" style="left:1128px" width="22" height="40" viewBox="0 0 22 40"><path d="M4 2l14 18L4 38" fill="none" stroke="#bbb" stroke-width="2"/></svg>

<article class="abs card" style="left:109px">
  <div class="inner">
    <div class="photo" role="img" aria-label="Concert crowd under bright stage lights" style="background:linear-gradient(180deg,#e8e8f4,#b0509a 45%,#3a1640)"></div>
    <h3>The Harbor Amphitheater</h3>
    <div class="meta"><svg width="12" height="12" viewBox="0 0 12 12"><path d="M4 10V2l7-1v7" fill="none" stroke="#4fb8e8" stroke-width="1.5"/><circle cx="3" cy="10" r="1.8" fill="#4fb8e8"/><circle cx="10" cy="8" r="1.8" fill="#4fb8e8"/></svg>The Harbor Amphitheater<svg class="gap" width="12" height="12" viewBox="0 0 12 12"><circle cx="6" cy="4" r="3" fill="#4fb8e8"/><path d="M1 12a5 5 0 0 1 10 0z" fill="#4fb8e8"/></svg>08</div>
    <div class="meta"><svg width="12" height="12" viewBox="0 0 12 12"><circle cx="6" cy="6" r="5" fill="none" stroke="#4fb8e8" stroke-width="1.4"/><path d="M6 3v3h2.5" fill="none" stroke="#4fb8e8" stroke-width="1.4"/></svg>JUNE 5 - 8:00PM - OCTOBER 3-9:00PM</div>
    <div class="meta"><svg width="10" height="13" viewBox="0 0 10 13"><path d="M5 13S0 7 0 5a5 5 0 0 1 10 0c0 2-5 8-5 8z" fill="#4fb8e8"/><circle cx="5" cy="5" r="1.8" fill="#0c0c0d"/></svg>Lanford Park Hotel, Newyork</div>
  </div>
</article>
<article class="abs card" style="left:444px">
  <div class="inner">
    <div class="photo" role="img" aria-label="Stage with performers and spotlights above the crowd" style="background:linear-gradient(180deg,#9a8a7a,#5a463a 45%,#1e1612)"></div>
    <h3>The Harbor Amphitheater</h3>
    <div class="meta"><svg width="12" height="12" viewBox="0 0 12 12"><path d="M4 10V2l7-1v7" fill="none" stroke="#4fb8e8" stroke-width="1.5"/><circle cx="3" cy="10" r="1.8" fill="#4fb8e8"/><circle cx="10" cy="8" r="1.8" fill="#4fb8e8"/></svg>The Harbor Amphitheater<svg class="gap" width="12" height="12" viewBox="0 0 12 12"><circle cx="6" cy="4" r="3" fill="#4fb8e8"/><path d="M1 12a5 5 0 0 1 10 0z" fill="#4fb8e8"/></svg>08</div>
    <div class="meta"><svg width="12" height="12" viewBox="0 0 12 12"><circle cx="6" cy="6" r="5" fill="none" stroke="#4fb8e8" stroke-width="1.4"/><path d="M6 3v3h2.5" fill="none" stroke="#4fb8e8" stroke-width="1.4"/></svg>JUNE 5 - 8:00PM - OCTOBER 3-9:00PM</div>
    <div class="meta"><svg width="10" height="13" viewBox="0 0 10 13"><path d="M5 13S0 7 0 5a5 5 0 0 1 10 0c0 2-5 8-5 8z" fill="#4fb8e8"/><circle cx="5" cy="5" r="1.8" fill="#0c0c0d"/></svg>Lanford Park Hotel, Newyork</div>
  </div>
</article>
<article class="abs card" style="left:780px">
  <div class="inner">
    <div class="photo" role="img" aria-label="Guitarist on stage in blue light" style="background:linear-gradient(180deg,#2a6ad8,#123c8c 50%,#0a1530)"></div>
    <h3>The Harbor Amphitheater</h3>
    <div class="meta"><svg width="12" height="12" viewBox="0 0 12 12"><path d="M4 10V2l7-1v7" fill="none" stroke="#4fb8e8" stroke-width="1.5"/><circle cx="3" cy="10" r="1.8" fill="#4fb8e8"/><circle cx="10" cy="8" r="1.8" fill="#4fb8e8"/></svg>The Harbor Amphitheater<svg class="gap" width="12" height="12" viewBox="0 0 12 12"><circle cx="6" cy="4" r="3" fill="#4fb8e8"/><path d="M1 12a5 5 0 0 1 10 0z" fill="#4fb8e8"/></svg>08</div>
    <div class="meta"><svg width="12" height="12" viewBox="0 0 12 12"><circle cx="6" cy="6" r="5" fill="none" stroke="#4fb8e8" stroke-width="1.4"/><path d="M6 3v3h2.5" fill="none" stroke="#4fb8e8" stroke-width="1.4"/></svg>JUNE 5 - 8:00PM - OCTOBER 3-9:00PM</div>
    <div class="meta"><svg width="10" height="13" viewBox="0 0 10 13"><path d="M5 13S0 7 0 5a5 5 0 0 1 10 0c0 2-5 8-5 8z" fill="#4fb8e8"/><circle cx="5" cy="5" r="1.8" fill="#0c0c0d"/></svg>Lanford Park Hotel, Newyork</div>
  </div>
</article>

<section class="abs videos" role="img" aria-label="Dark blue concert crowd backdrop"></section>
<h2 class="abs section-title" style="top:1452px">Latest Video</h2>

<div class="abs video" style="left:109px;top:1514px;background:linear-gradient(135deg,#c0501e,#5a1a10)" role="img" aria-label="Band performing under orange light"><span class="play"></span><span class="date">7 MARCH,2015</span></div>
<div class="abs video" style="left:444px;top:1514px;background:linear-gradient(135deg,#8a8a8e,#3a2a22)" role="img" aria-label="Band on stage with guitars"><span class="play"></span><span class="date">7 MARCH,2015</span></div>
<div class="abs video" style="left:780px;top:1514px;background:#ffffff;border-color:#ddd" role="img" aria-label="World map made of blue dots"></div>
<div class="abs video" style="left:109px;top:1686px;background:linear-gradient(135deg,#3a3aa0,#1a1440)" role="img" aria-label="Performer in purple stage light"><span class="play"></span><span class="date">7 MARCH,2015</span></div>
<div class="abs video" style="left:444px;top:1686px;background:linear-gradient(135deg,#e89a30,#5a2408)" role="img" aria-label="Stage with flames and crowd"><span class="play"></span><span class="date">7 MARCH,2015</span></div>
<div class="abs video featured" style="left:780px;top:1706px;height:186px;background:linear-gradient(135deg,#c8a47a,#6a4a30)" role="img" aria-label="Guitarist in warm light">
  <div class="label">Awesome Bass<small>Rock</small></div>
  <div class="bar"><span>DETAIL</span><span>+ ADD TO PLAYLIST</span></div>
</div>
<div class="abs btn-blue btn-outline-blue" style="left:366px;top:1860px;width:142px;height:31px;font-size:13px">View More Video</div>

<section class="abs upcoming"></section>
<h2 class="abs section-title" style="top:1950px">Upcoming Events</h2>

<div class="abs event-img" style="left:109px;top:2030px;background:linear-gradient(135deg,#e040b0,#4a0a40)" role="img" aria-label="Microphone on stage in pink light"></div>
<div class="abs event-info" style="left:357px;top:2024px">
  <h3>The Harbor Amphitheater</h3>
  <div class="meta"><svg width="11" height="11" viewBox="0 0 11 11"><rect x="0.5" y="1.5" width="10" height="9" fill="none" stroke="#fff"/><path d="M0 4h11" stroke="#fff"/></svg>JUNE 5 - 8:00PM - OCTOBER 3-9:00PM</div>
  <div class="meta"><svg width="10" height="13" viewBox="0 0 10 13"><path d="M5 13S0 7 0 5a5 5 0 0 1 10 0c0 2-5 8-5 8z" fill="#fff"/><circle cx="5" cy="5" r="1.8" fill="#133a54"/></svg>Lanford Park Hotel, Newyork</div>
  <div class="ev-btns"><span>Buy Tickets</span><span>Detail</span></div>
</div>
<div class="abs event-img" style="left:615px;top:2030px;background:linear-gradient(135deg,#f07a20,#5a1a08)" role="img" aria-label="Guitarist under orange stage light"></div>
<div class="abs event-info" style="left:863px;top:2024px">
  <h3>The Harbor Amphitheater</h3>
  <div class="meta"><svg width="11" height="11" viewBox="0 0 11 11"><rect x="0.5" y="1.5" width="10" height="9" fill="none" stroke="#fff"/><path d="M0 4h11" stroke="#fff"/></svg>JUNE 5 - 8:00PM - OCTOBER 3-9:00PM</div>
  <div class="meta"><svg width="10" height="13" viewBox="0 0 10 13"><path d="M5 13S0 7 0 5a5 5 0 0 1 10 0c0 2-5 8-5 8z" fill="#fff"/><circle cx="5" cy="5" r="1.8" fill="#133a54"/></svg>Lanford Park Hotel, Newyork</div>
  <div class="ev-btns"><span>Buy Tickets</span><span>Detail</span></div>
</div>

<div class="abs divider"></div>

<div class="abs event-img" style="left:109px;top:2237px;background:linear-gradient(135deg,#7a40b0,#1a0a30)" role="img" aria-label="DJ behind decks in violet light"></div>
<div class="abs event-info" style="left:357px;top:2232px">
  <h3>The Harbor Amphitheater</h3>
  <div class="meta"><svg width="11" height="11" viewBox="0 0 11 11"><rect x="0.5" y="1.5" width="10" height="9" fill="none" stroke="#fff"/><path d="M0 4h11" stroke="#fff"/></svg>JUNE 5 - 8:00PM - OCTOBER 3-9:00PM</div>
  <div class="meta"><svg width="10" height="13" viewBox="0 0 10 13"><path d="M5 13S0 7 0 5a5 5 0 0 1 10 0c0 2-5 8-5 8z" fill="#fff"/><circle cx="5" cy="5" r="1.8" fill="#133a54"/></svg>Lanford Park Hotel, Newyork</div>
  <div class="ev-btns"><span>Buy Tickets</span><span>Detail</span></div>
</div>
<div class="abs event-img" style="left:615px;top:2237px;background:linear-gradient(135deg,#3050e0,#d02060 70%,#200818)" role="img" aria-label="Club stage with blue and red lasers"></div>
<div class="abs event-info" style="left:863px;top:2232px">
  <h3>The Harbor Amphitheater</h3>
  <div class="meta"><svg width="11" height="11" viewBox="0 0 11 11"><rect x="0.5" y="1.5" width="10" height="9" fill="none" stroke="#fff"/><path d="M0 4h11" stroke="#fff"/></svg>JUNE 5 - 8:00PM - OCTOBER 3-9:00PM</div>
  <div class="meta"><svg width="10" height="13" viewBox="0 0 10 13"><path d="M5 13S0 7 0 5a5 5 0 0 1 10 0c0 2-5 8-5 8z" fill="#fff"/><circle cx="5" cy="5" r="1.8" fill="#133a54"/></svg>Lanford Park Hotel, Newyork</div>
  <div class="ev-btns"><span>Buy Tickets</span><span>Detail</span></div>
</div>

<div class="abs btn-blue btn-outline-blue" style="left:529px;top:2400px;width:234px;height:31px;font-size:13px">View More Upcoming Events</div>

<footer class="abs footer">
  <div class="abs fcol" style="left:109px;top:28px">
    <h4>Quick Links</h4>
    <ul class="links"><li>Home</li><li>Events</li><li>Map</li><li>Carpooling</li><li>Photos</li><li>Contact Us</li></ul>
  </div>
  <div class="abs fcol" style="left:308px;top:28px;width:200px">
    <h4>Newsletter Signup</h4>
    <p>Lorem ipsum dolor sit amet,consecte adipiscing elit, sed diam nonummy ni euismod tincidunt.</p>
    <div class="email">Email Address</div>
    <div class="btn-blue subscribe">SUBSCRIBE</div>
  </div>
  <div class="abs fcol" style="left:602px;top:28px;width:200px">
    <h4>Contact Detail</h4>
    <div class="contact-row"><svg width="10" height="14" viewBox="0 0 10 13"><path d="M5 13S0 7 0 5a5 5 0 0 1 10 0c0 2-5 8-5 8z" fill="#fff"/><circle cx="5" cy="5" r="1.8" fill="#222"/></svg><span>Lorem ipsum dolor sit amet consecte adipiscing elit, diam nonummy</span></div>
    <div class="contact-row"><svg width="12" height="12" viewBox="0 0 12 12"><path d="M2 1h3l1 3-2 1a7 7 0 0 0 3 3l1-2 3 1v3c-6 0-10-4-10-10z" fill="#fff"/></svg><span>(010) 555 0142</span></div>
    <div class="contact-row"><svg width="12" height="12" viewBox="0 0 12 12"><rect x="1" y="3" width="10" height="8" fill="#fff"/><rect x="3" y="1" width="6" height="3" fill="#fff"/></svg><span>(011) 555 0187</span></div>
    <div class="contact-row"><svg width="12" height="10" viewBox="0 0 12 10"><rect width="12" height="9" fill="#fff"/><path d="M0 0l6 5 6-5" fill="none" stroke="#222"/></svg><span>info@ploxevents.com</span></div>
  </div>
  <div class="abs fcol" style="left:876px;top:28px">
    <h4>Map</h4>
  </div>
  <div class="abs" style="left:876px;top:71px;width:214px;height:127px;background:linear-gradient(135deg,#ecebe6,#d8d6cf);border:1px solid #999" role="img" aria-label="Street map showing the office location, Kelvin Row Depot"></div>
</footer>

<div class="abs bottom">
  <span class="abs" style="left:109px;top:11px">Copyright © 2015 ploxevents.</span>
  <span class="abs" style="left:902px;top:11px">Privacy Policy &nbsp; | &nbsp; Terms &amp; Conditions</span>
</div>

</body>
</html>
```